Brevant Business Card

I have a business that is called "Brevant Electrical Products LTD" My company deals with top of the range laptops and mobile phones that are exclusive. I need a business card that will be eye catching but not over complicated.

Target Market(s)

Adults aged 19 to 50
Upper middle class

Industry/Entity Type

Business

Requirements
Must have
• Company name/logo (file attached)
• It must have my contact information which is:

• Name: Dale Marwick

• Position: Managing Director 

• Business Address: 7 Hapton Row, London, W4 9QD

• Contact Number: 02085193604
• Mobile: 07814260537
• Email: info@brevant-goods.co.uk
Nice to have
• Simple and stylish
• Eye catching

```html
<!DOCTYPE html>
<html lang="en">
<head>
<meta charset="utf-8">
<title>Brevant Electrical Products – Business Card</title>
<link rel="stylesheet" href="https://fonts.googleapis.com/css2?family=Mulish:wght@300;400;700;800&display=swap">
<style>
  :root {
    --card-teal: #135874;
    --card-teal-deep: #0d4660;
    --accent-cyan: #5ff6f2;
    --ink-white: #ffffff;
    --page-bg: #ffffff;
  }
  * { margin: 0; padding: 0; box-sizing: border-box; }
  html, body {
    width: 1200px; height: 1031px; overflow: hidden;
    background: var(--page-bg);
    font-family: "Mulish", "Century Gothic", sans-serif;
    color: var(--ink-white);
  }
  .canvas { position: relative; width: 1200px; height: 1031px; }

  .card {
    position: absolute;
    width: 717px; height: 413px;
    background: var(--card-teal);
    overflow: hidden;
  }
  .card--front { left: 183px; top: 169px; }
  .card--back  { left: 300px; top: 619px; }

  .card__frame {
    position: absolute;
    left: 21px; top: 19px; right: 22px; bottom: 18px;
    border: 2px solid var(--ink-white);
  }

  .card__texture {
    position: absolute;
    border-radius: 50%;
    background: radial-gradient(circle at 45% 45%, #1a6a86 0%, #155f7c 55%, var(--card-teal-deep) 100%);
    box-shadow: 8px 10px 24px rgba(5, 35, 50, 0.55);
  }
  .card--front .card__texture { left: -20px; top: -110px; width: 270px; height: 270px; }
  .card--back  .card__texture { left: 483px; top: -9px; width: 234px; height: 234px; }

  .brand {
    position: absolute;
    left: 97px; top: 112px; width: 550px;
    text-align: center;
  }
  .brand__name {
    display: block;
    font-weight: 300;
    font-size: 124px;
    line-height: 1;
    letter-spacing: 2px;
    color: var(--accent-cyan);
  }
  .brand__tagline {
    display: block;
    margin-top: 12px;
    font-weight: 700;
    font-size: 55px;
    line-height: 1;
    letter-spacing: 1px;
    color: var(--ink-white);
  }
  .address {
    position: absolute;
    left: 0; right: 0; top: 356px;
    text-align: center;
    padding-left: 40px;
    font-weight: 400;
    font-size: 17px;
  }

  .person { position: absolute; left: 52px; top: 66px; }
  .person__name {
    font-weight: 700;
    font-size: 45px;
    line-height: 1;
  }
  .person__role {
    margin-left: 163px;
    margin-top: 8px;
    font-weight: 700;
    font-size: 23px;
    line-height: 1;
  }

  .contact { position: absolute; left: 173px; top: 232px; }
  .contact__row {
    display: flex;
    font-size: 34px;
    line-height: 40px;
  }
  .contact__label { width: 128px; font-weight: 700; }
  .contact__value { font-weight: 300; }

  .email {
    position: absolute;
    left: 0; right: 0; top: 338px;
    text-align: center;
    padding-left: 30px;
    font-weight: 700;
    font-size: 31px;
  }
</style>
</head>
<body>
<main class="canvas">

  <section class="card card--front" aria-label="Business card front">
    <div class="card__texture" role="img" aria-label="Circular textured fabric-like decoration in deep teal tones"></div>
    <div class="card__frame"></div>
    <h1 class="brand">
      <span class="brand__name">BREVANT</span>
      <span class="brand__tagline">Electrical Products</span>
    </h1>
    <p class="address">7 Hapton Row, London W4 9QD</p>
  </section>

  <section class="card card--back" aria-label="Business card back">
    <div class="card__texture" role="img" aria-label="Circular textured fabric-like decoration in deep teal tones"></div>
    <div class="card__frame"></div>
    <div class="person">
      <h2 class="person__name">Dale Marwick</h2>
      <p class="person__role">Managing Director</p>
    </div>
    <div class="contact">
      <p class="contact__row"><span class="contact__label">Phone:</span><span class="contact__value">0 208 519 3604</span></p>
      <p class="contact__row"><span class="contact__label">Mobile:</span><span class="contact__value">0 781 426 0537</span></p>
    </div>
    <p class="email">info@brevant-goods.co.uk</p>
  </section>

</main>
</body>
</html>
```